Vantor Reach Unique Marketing Website Design

I am starting a new company that is a thought leader in the marketing consulting space. The company is called Vantor Reach. We intend to build a Wordpress site on the Astra Theme with the Spectra builder. Our goal is to become the leading voice that empowers high-ticket service business leaders to become Vantor Reach by equipping them with the cutting-edge frameworks and decision grade intelligence taught in leading business schools. What we are looking for is a website design that is clean and professional, making some use of white space well also being eye catching and distinctive in the consulting space. We will probably want to have a video on the homepage not in the hero section, but just below to explain the company and what we do. Our tagline is "Be found. Be chosen." I have attached a brand guide with some messaging, our typography choices, and our color system. The full site will have a primary nav that is four pages - About us, Services, Insights (essentially a blog), and Contact Us. The goal of this project is to develop an art direction that I can give to a designer to build loads of new pages.

Target Market(s)

Business owners (mostly male) from 30-60 years old, looking to fix their sales and marketing funnel.

Industry/Entity Type

Marketing consulting

Font styles to use
Sans Serif

Requirements
Must have
• A clean, professional design that builds trust with owners of high-ticket service businesses. We need a space for explainer video, and sections that tell prospects what we do. Would also like to have a blog carousel.
Nice to have
• Social feeds, if possible. See attached documents for colors and fonts.
Should not have
• Our feel is professional enough to be trustworthy, but unique enough to be memorable. Cartoon ideas do not meet the professional test, and we do not want the website to appear feminine.

```html
<!DOCTYPE html>
<html lang="en">
<head>
<meta charset="utf-8">
<title>Vantor Reach — Be Found. Be Chosen</title>
<link href="https://fonts.googleapis.com/css2?family=Oswald:wght@500;600;700&family=Inter:wght@400;500;600&display=swap" rel="stylesheet">
<style>
:root{
  --purple:#a97ff5;
  --purple-deep:#9468ec;
  --heading:#a878f0;
  --blue:#29b2ea;
  --lavender:#dfe1f6;
  --ink:#1c1c24;
  --text:#4a4a55;
  --white:#ffffff;
}
*{margin:0;padding:0;box-sizing:border-box}
html,body{width:1200px;height:3285px;overflow:hidden}
body{font-family:"Inter",Arial,sans-serif;color:var(--text);background:var(--white);position:relative}
.abs{position:absolute}
h1,h2,h3{font-family:"Oswald",Arial Narrow,sans-serif;font-weight:600}
.btn{position:absolute;background:var(--blue);color:var(--white);font-size:15px;border-radius:4px;display:flex;align-items:center;justify-content:center;text-decoration:none}
.brand{font-family:"Inter",Arial,sans-serif;font-weight:600;color:var(--white);letter-spacing:1px}

/* hero */
.hero{top:0;left:0;width:1200px;height:630px;background:linear-gradient(120deg,#8e64e6 0%,#a47cf3 45%,#b896f7 100%)}
.hero .brand{left:111px;top:28px;font-size:30px}
.nav{position:absolute;top:33px;left:611px;display:flex;gap:0}
.nav a{position:absolute;color:var(--white);text-decoration:none;font-size:16px;white-space:nowrap}
.nav a.active{text-decoration:underline;font-weight:600}
.hero h1{left:108px;top:212px;font-size:82px;color:var(--white);font-weight:700;letter-spacing:1px}
.hero p{left:111px;top:332px;width:660px;font-size:17px;line-height:26px;color:var(--white)}

/* section heads */
.title{font-size:46px;color:var(--heading)}
.center{left:0;width:1200px;text-align:center}
.lead{font-size:15px;line-height:26px;color:var(--text)}

/* what we do */
.what{top:630px;left:0;width:1200px;height:608px;background:var(--lavender)}
.card{position:absolute;top:239px;width:306px;height:219px;background:var(--white);border-radius:6px;border-bottom:3px solid var(--purple);padding:28px 21px}
.card svg{display:block;width:52px;height:52px}
.card h3{font-size:22px;color:var(--ink);margin-top:20px;font-weight:500}
.card p{font-size:12.5px;line-height:18px;margin-top:12px;text-align:justify}

/* about */
.about .title{left:111px;top:1310px}
.about .strong{left:111px;top:1385px;width:520px;font-size:15px;line-height:26px;color:var(--ink);font-weight:500}
.about .body{left:111px;width:515px;font-size:15px;line-height:26px;text-align:justify}
.video-back{left:799px;top:1347px;width:290px;height:229px;background:var(--purple);border-radius:4px}
.video{left:702px;top:1369px;width:364px;height:288px;background:linear-gradient(135deg,#c9c4bd,#8b8680 55%,#5e5a57);border-radius:6px}
.play{left:856px;top:1484px;width:56px;height:56px;border-radius:50%;background:var(--blue);border:4px solid var(--white)}

/* why */
.feat h3{position:absolute;font-size:22px;color:var(--ink);font-weight:500}
.feat p{position:absolute;font-size:12.5px;line-height:18px;width:270px}
.feat.left h3,.feat.left p{text-align:right}
.icon{position:absolute;width:62px;height:62px;border-radius:50%;background:var(--blue);display:flex;align-items:center;justify-content:center}

/* blogs */
.blogs{top:2398px;left:0;width:1200px;height:675px;background:var(--lavender)}
.post{position:absolute;top:239px;width:306px}
.post .photo{width:306px;height:188px;border-radius:4px}
.post .meta{margin-top:26px;font-size:12px;color:var(--purple)}
.post h3{font-size:19px;color:var(--ink);font-weight:500;margin-top:8px}
.post p{font-size:12.5px;line-height:18px;margin-top:8px;text-align:justify}
.post a{display:inline-block;margin-top:8px;font-size:15px;color:var(--blue)}

/* footer */
.footer{top:3073px;left:0;width:1200px;height:212px;background:linear-gradient(120deg,#a07af0,#b690f6 50%,#9d74ee)}
.footer .brand{left:0;width:1200px;text-align:center;top:62px;font-size:30px}
.footer .links a{position:absolute;top:127px;color:var(--white);font-size:16px;text-decoration:none}
.footer .rule{left:111px;top:159px;width:978px;height:1px;background:rgba(255,255,255,.5)}
.footer .copy{left:0;width:1200px;text-align:center;top:174px;font-size:10px;color:var(--white)}
</style>
</head>
<body>

<header class="abs hero" role="img" aria-label="Photo of two consultants in a meeting, purple tint">
  <div class="abs brand">VANTOR REACH</div>
  <nav class="nav">
    <a class="active" style="left:0">Home</a>
    <a style="left:93px">About</a>
    <a style="left:184px">Services</a>
    <a style="left:295px">Insights</a>
    <a style="left:399px">Contact Us</a>
  </nav>
  <h1 class="abs">Be Found. Be Chosen</h1>
  <p class="abs">We help high-ticket service businesses master demand using proven frameworks and decision-grade intelligence.</p>
  <a class="btn" style="left:111px;top:396px;width:190px;height:40px">Explore Our Thinking</a>
</header>

<section class="abs what">
  <h2 class="abs title center" style="top:72px">What We Do</h2>
  <p class="abs lead" style="left:210px;top:144px;width:780px;text-align:center">Lorem ipsum dolor sit amet, consectetur adipiscing elit, sed do eiusmod tempor incididunt ut labore et dolore magna aliqua. Quis ipsum suspendisse ultrices gravida.</p>

  <div class="card" style="left:111px">
    <svg viewBox="0 0 52 52" fill="#a97ff5"><circle cx="16" cy="12" r="5"/><circle cx="27" cy="12" r="5"/><circle cx="38" cy="12" r="5"/><circle cx="36" cy="30" r="9" fill="none" stroke="#a97ff5" stroke-width="3"/><circle cx="36" cy="30" r="3"/><circle cx="12" cy="31" r="5"/><path d="M2 50c0-8 5-12 10-12s10 4 10 12z"/><path d="M24 50c0-6 5-9 12-9s12 3 12 9z"/></svg>
    <h3>Demand Strategy</h3>
    <p>Lorem ipsum dolor sit amet, consectetur adipiscing elit, sed do eiusmod tempor inc ididunt ut labore et dolore</p>
  </div>
  <div class="card" style="left:448px">
    <svg viewBox="0 0 52 52" fill="#a97ff5"><rect x="2" y="36" width="9" height="14"/><rect x="15" y="30" width="9" height="20"/><rect x="28" y="24" width="9" height="26"/><rect x="41" y="16" width="9" height="34"/><path d="M3 28l14-12 10 7 16-17" fill="none" stroke="#a97ff5" stroke-width="3"/><path d="M38 3h10v10z"/></svg>
    <h3>Go-to-Market Systems</h3>
    <p>Lorem ipsum dolor sit amet, consectetur adipiscing elit, sed do eiusmod tempor inc ididunt ut labore et dolore</p>
  </div>
  <div class="card" style="left:783px">
    <svg viewBox="0 0 52 52" fill="#a97ff5"><circle cx="24" cy="12" r="6"/><rect x="18" y="1" width="12" height="6" rx="3"/><path d="M12 34c0-9 5-14 12-14s12 5 12 14z"/><rect x="6" y="34" width="40" height="5"/><rect x="10" y="39" width="4" height="11"/><rect x="38" y="39" width="4" height="11"/><rect x="36" y="24" width="12" height="8"/></svg>
    <h3>Executive Advisory</h3>
    <p>Lorem ipsum dolor sit amet, consectetur adipiscing elit, sed do eiusmod tempor inc ididunt ut labore et dolore</p>
  </div>

  <a class="btn" style="left:539px;top:484px;width:122px;height:39px">View More</a>
</section>

<section class="about">
  <h2 class="abs title" style="left:111px;top:1310px">About Us</h2>
  <p class="abs strong">Lorem ipsum dolor sit amet, consectetur adipiscing elit, sed do eiusmod tempor incididunt ut labore et dolore magna aliqua.</p>
  <p class="abs body" style="top:1446px">Sed ut perspiciatis unde omnis iste natus error sit voluptatem accusantium doloremque laudantium, totam rem aperiam, eaque ipsa quae ab illo inventore veritatis et quasi architecto beatae vitae dicta sunt explicabo. Nemo enim ipsam voluptatem quia voluptas sit aspernatur aut odit aut fugit, sed quia consequuntur magni dolores eos qui</p>
  <p class="abs body" style="top:1583px">Lorem ipsum dolor sit amet, consectetur adipiscing elit, sed do eiusmod tempor incididunt ut labore et dolore magna aliqua.</p>
  <a class="btn" style="left:111px;top:1651px;width:122px;height:40px">Read More</a>

  <div class="abs video-back"></div>
  <svg class="abs" style="left:680px;top:1585px" width="90" height="85" viewBox="0 0 90 85" fill="#1c1c24">
    <g><circle cx="3" cy="3" r="1.6"/><circle cx="3" cy="16" r="1.6"/><circle cx="3" cy="29" r="1.6"/><circle cx="3" cy="42" r="1.6"/><circle cx="3" cy="55" r="1.6"/><circle cx="3" cy="68" r="1.6"/><circle cx="3" cy="81" r="1.6"/>
    <circle cx="16" cy="3" r="1.6"/><circle cx="16" cy="16" r="1.6"/><circle cx="16" cy="29" r="1.6"/><circle cx="16" cy="42" r="1.6"/><circle cx="16" cy="55" r="1.6"/><circle cx="16" cy="68" r="1.6"/><circle cx="16" cy="81" r="1.6"/>
    <circle cx="29" cy="81" r="1.6"/><circle cx="42" cy="81" r="1.6"/><circle cx="55" cy="81" r="1.6"/><circle cx="68" cy="81" r="1.6"/><circle cx="81" cy="81" r="1.6"/></g>
  </svg>
  <div class="abs video" role="img" aria-label="Explainer video still: team meeting in a glass-walled office"></div>
  <div class="abs play"><svg width="48" height="48" viewBox="0 0 48 48"><path d="M19 14l15 10-15 10z" fill="#fff"/></svg></div>
</section>

<section class="why">
  <h2 class="abs title center" style="top:1766px">Why Leaders Choose Vantor Reach</h2>
  <p class="abs lead" style="left:210px;top:1838px;width:780px;text-align:center">Lorem ipsum dolor sit amet, consectetur adipiscing elit, sed do eiusmod tempor incididunt ut labore et dolore magna aliqua. Quis ipsum suspendisse ultrices gravida.</p>

  <svg class="abs" style="left:380px;top:1920px" width="440" height="420" viewBox="0 0 440 420">
    <circle cx="220" cy="210" r="208" fill="none" stroke="#1c1c24" stroke-width="1.3" stroke-dasharray="6 6"/>
  </svg>
  <div class="abs" style="left:429px;top:1966px;width:342px;height:342px;border-radius:50%;background:var(--purple)" role="img" aria-label="Portrait of a smiling business consultant at a laptop"></div>
  <div class="abs" style="left:380px;top:2315px;width:440px;height:85px;background:var(--white)"></div>

  <div class="feat left">
    <h3 style="left:83px;top:1980px;width:270px">Business-School Rigor</h3>
    <p style="left:83px;top:2016px">Lorem ipsum dolor sit amet, consectetur adipiscing elit, sed do eiusmod tempor inc</p>
    <h3 style="left:83px;top:2203px;width:270px">Built for High-Ticket</h3>
    <p style="left:83px;top:2239px">Lorem ipsum dolor sit amet, consectetur adipiscing elit, sed do eiusmod tempor inc</p>
  </div>
  <div class="feat right">
    <h3 style="left:846px;top:1980px;width:300px">Built on Proven Frameworks</h3>
    <p style="left:847px;top:2016px">Lorem ipsum dolor sit amet, consectetur adipiscing elit, sed do eiusmod tempor inc</p>
    <h3 style="left:846px;top:2203px;width:300px">Decision-Grade Intelligence</h3>
    <p style="left:847px;top:2239px">Lorem ipsum dolor sit amet, consectetur adipiscing elit, sed do eiusmod tempor inc</p>
  </div>

  <div class="icon" style="left:368px;top:1991px"><svg width="30" height="30" viewBox="0 0 30 30" fill="#fff"><rect x="10" y="4" width="10" height="5" rx="1" fill="none" stroke="#fff" stroke-width="2.5"/><rect x="2" y="9" width="26" height="18" rx="2"/><rect x="2" y="16" width="26" height="2" fill="#29b2ea"/></svg></div>
  <div class="icon" style="left:768px;top:1991px"><svg width="34" height="34" viewBox="0 0 34 34" fill="none" stroke="#fff" stroke-width="2"><circle cx="17" cy="17" r="7"/><circle cx="17" cy="17" r="2.5" fill="#fff"/><path d="M17 3v7M17 24v7M4 10l7 4M23 20l7 4M4 24l7-4M23 14l7-4"/></svg></div>
  <div class="icon" style="left:368px;top:2214px"><svg width="34" height="34" viewBox="0 0 34 34" fill="none" stroke="#fff" stroke-width="2.5"><path d="M6 26a13 13 0 1 1 22 0"/><path d="M17 18l6-7"/><circle cx="17" cy="19" r="2.5" fill="#fff"/></svg></div>
  <div class="icon" style="left:768px;top:2214px"><svg width="34" height="34" viewBox="0 0 34 34" fill="#fff"><path d="M17 2l6 7h-4v9l8 6-2 3-8-6-8 6-2-3 8-6V9h-4z"/></svg></div>
</section>

<section class="abs blogs">
  <h2 class="abs title" style="left:111px;top:73px">Latest Blogs</h2>
  <p class="abs lead" style="left:111px;top:146px;width:770px">Lorem ipsum dolor sit amet, consectetur adipiscing elit, sed do eiusmod tempor incididunt ut labore et dolore magna aliqua. Quis ipsum suspendisse ultrices gravida.</p>
  <a class="btn" style="left:967px;top:157px;width:122px;height:39px">View More</a>

  <article class="post" style="left:111px">
    <div class="photo" role="img" aria-label="Consultant smiling during a client meeting" style="background:linear-gradient(135deg,#5a5560,#9a9fa8 60%,#c8ccd2)"></div>
    <div class="meta">▦ Jan 28th, 2026 &nbsp;|&nbsp; ● By Admin</div>
    <h3>Lorem ipsum dolor sit amet, con</h3>
    <p>Lorem ipsum dolor sit amet, consectetur adipiscing elit, sed do eiusmod tempor incididunt ut labore et dolore magna aliqua.</p>
    <a>Read More</a>
  </article>
  <article class="post" style="left:448px">
    <div class="photo" role="img" aria-label="Hands reviewing charts on a tablet" style="background:linear-gradient(135deg,#c9a24a,#8a8f99 50%,#2f3440)"></div>
    <div class="meta">▦ Jan 28th, 2026 &nbsp;|&nbsp; ● By Admin</div>
    <h3>Lorem ipsum dolor sit amet, con</h3>
    <p>Lorem ipsum dolor sit amet, consectetur adipiscing elit, sed do eiusmod tempor incididunt ut labore et dolore magna aliqua.</p>
    <a>Read More</a>
  </article>
  <article class="post" style="left:784px">
    <div class="photo" role="img" aria-label="Team discussion around an office table" style="background:linear-gradient(135deg,#4a4842,#b8b2a8 55%,#e2ddd4)"></div>
    <div class="meta">▦ Jan 28th, 2026 &nbsp;|&nbsp; ● By Admin</div>
    <h3>Lorem ipsum dolor sit amet, con</h3>
    <p>Lorem ipsum dolor sit amet, consectetur adipiscing elit, sed do eiusmod tempor incididunt ut labore et dolore magna aliqua.</p>
    <a>Read More</a>
  </article>
</section>

<footer class="abs footer" role="img" aria-label="Desk with business papers, purple tint">
  <div class="abs brand">VANTOR REACH</div>
  <nav class="links">
    <a style="left:360px">Home</a>
    <a style="left:451px">About</a>
    <a style="left:543px">Services</a>
    <a style="left:653px">Insights</a>
    <a style="left:758px">Contact Us</a>
  </nav>
  <div class="abs rule"></div>
  <div class="abs copy">Copyright © 2026 Vantor Reach. All rights reserved.</div>
</footer>

</body>
</html>
```